Harborline Energy - needs a business card

Harborline Energy is a U.S. based diesel sourcing and distribution company that supports American oil & gas fields through providing quality product and consistent services.

Target Market(s)

Oil and Gas

Contact Information for Business Card

The background of the card must be white to ensure the logo pops.

Font styles to use
Serif
Sans Serif

Colors

Designer to choose colors to be used in the design.

Requirements
Must have
• Front of Card: Tag line: Harborline Energy, Powering America's Oil & Gas fields.
• Not sure if you guys do this part but just in case...
• Dale Menschow
• Owner/CEO
• C:555.318.4076
• E:Dmenschow@harborlineenergy.example
• W:Harborlineenergy.example
• Locations: Servicing the Powder River, DJ basin and Bakken formations.
• Back of Card: " Frac fueling is what we do. We understand how important diesel fuel is to your operation, which is why our main service line is Frac fueling. We assure our supply and stand by our service"

```html
<!DOCTYPE html>
<html lang="en">
<head>
<meta charset="utf-8">
<title>Harborline Energy – Business Card</title>
<link rel="stylesheet" href="https://fonts.googleapis.com/css2?family=Barlow+Condensed:ital,wght@1,700&family=Open+Sans:ital,wght@0,400;0,600;0,700;1,400;1,600&display=swap">
<style>
  :root {
    --navy: #1c2d5a;
    --red: #c8202f;
    --white: #ffffff;
    --ink: #1f1f24;
    --stage: #ececec;
    --watermark: #d6d9e3;
  }
  * { box-sizing: border-box; margin: 0; padding: 0; }
  html, body { width: 1200px; height: 800px; overflow: hidden; }
  body {
    background: var(--stage);
    font-family: "Open Sans", Arial, sans-serif;
    color: var(--ink);
    position: relative;
  }
  .card {
    position: absolute;
    top: 245px;
    width: 540px;
    height: 309px;
    overflow: hidden;
    box-shadow: 0 2px 6px rgba(0,0,0,0.12);
  }

  /* Back of card */
  .card-back { left: 40px; background: var(--navy); color: var(--white); }
  .card-back .brand {
    position: absolute; top: 92px; left: 0; right: 0;
    display: flex; align-items: center; justify-content: center; gap: 12px;
  }
  .card-back .brand-dot { width: 22px; height: 22px; border-radius: 50%; background: var(--red); }
  .card-back .brand-name {
    font-weight: 700; font-size: 34px; letter-spacing: 0.5px; color: var(--white);
  }
  .card-back .quote {
    position: absolute; left: 50px; right: 50px; top: 178px;
    font-weight: 600; font-size: 12.5px; line-height: 1.55; text-align: center;
  }

  /* Front of card */
  .card-front { left: 620px; background: var(--white); }
  .watermark {
    position: absolute; left: 14px; top: 118px;
    width: 120px; height: 120px; border-radius: 50%;
    background: var(--watermark); opacity: 0.6;
  }
  .person { position: absolute; left: 46px; top: 26px; }
  .person-name {
    font-family: "Barlow Condensed", "Arial Narrow", sans-serif;
    font-style: italic; font-weight: 700; font-size: 24px;
    letter-spacing: 0.3px; text-transform: uppercase; line-height: 1;
  }
  .person-title { font-size: 9px; margin-top: 2px; }
  .name-rule {
    position: absolute; left: 46px; top: 64px;
    width: 246px; height: 2px; background: var(--red);
  }
  .contact {
    position: absolute; left: 46px; top: 74px;
    font-size: 12px; line-height: 1.6;
    display: grid; grid-template-columns: 48px auto;
  }
  .locations {
    position: absolute; left: 46px; top: 158px;
    font-size: 12px; line-height: 1.5;
  }
  .locations .indent { padding-left: 72px; display: block; }
  .brand-front {
    position: absolute; right: 34px; top: 214px;
    display: flex; align-items: center; gap: 10px;
  }
  .brand-front .brand-dot { width: 18px; height: 18px; border-radius: 50%; background: var(--red); }
  .brand-front .brand-name { font-weight: 700; font-size: 25px; color: var(--navy); }
  .tagline-band {
    position: absolute; left: 0; right: 0; top: 116px;
    height: 0;
  }
  .card-front .band {
    position: absolute; left: 0; right: 0; bottom: 0; height: 22px;
    background: var(--red); color: var(--white);
    font-style: italic; font-size: 10px; letter-spacing: 0.4px;
    display: flex; align-items: center; padding-left: 140px;
  }
</style>
</head>
<body>

  <section class="card card-back" aria-label="Back of card">
    <div class="brand">
      <span class="brand-dot"></span>
      <span class="brand-name">Harborline Energy</span>
    </div>
    <p class="quote">“Frac fueling is what we do. We understand how important diesel fuel is to your operation, which is why our main service line is Frac fueling. We assure our supply and stand by our service”</p>
  </section>

  <section class="card card-front" aria-label="Front of card">
    <div class="watermark"></div>
    <div class="person">
      <h1 class="person-name">Dale Menschow</h1>
      <p class="person-title">CEO</p>
    </div>
    <div class="name-rule"></div>
    <div class="contact">
      <span>Phone</span><span>: 555.318.4076</span>
      <span>Email</span><span>: Dmenschow@harborlineenergy.example</span>
      <span>Web</span><span>: Harborlineenergy.example</span>
    </div>
    <p class="locations">Locations : Servicing the Powder River,<span class="indent">DJ basin and Bakken formations.</span></p>
    <div class="brand-front">
      <span class="brand-dot"></span>
      <span class="brand-name">Harborline Energy</span>
    </div>
    <div class="band">Harborline Energy, Powering America's Oil &amp; Gas fields.</div>
  </section>

</body>
</html>
```